serious, thorough, light and simple - that's my advice and mediations

My business card should combine my logo (uploaded file) and my homepage (https://fellor-mediation.webnestsite.com).

Contact Information for Business Card

Name: Sabine Fellor di Vanti
Phone: 076 412 58 94
mail: sfellor@postkiv.ch
web: www.fellor-di-vanti.ch

```html
<!DOCTYPE html>
<html lang="de">
<head>
<meta charset="utf-8">
<title>Business Card – Sabine Fellor di Vanti</title>
<link rel="stylesheet" href="https://fonts.googleapis.com/css2?family=Questrial&family=Hind:wght@400;500&display=swap">
<style>
  :root {
    --backdrop: #e6e7e9;
    --paper: #ffffff;
    --plum: #6f3650;
    --plum-dark: #5a1a35;
    --ink: #333333;
    --gold: #a8884f;
    --on-plum: #ffffff;
  }
  * { margin: 0; padding: 0; box-sizing: border-box; }
  html, body { width: 1169px; height: 1200px; overflow: hidden; background: var(--backdrop); }
  .canvas { position: relative; width: 1169px; height: 1200px; }

  .card { position: absolute; left: 154px; width: 861px; background: var(--paper); overflow: hidden; }
  .card--front { top: 93px; height: 492px; }
  .card--back { top: 616px; height: 491px; }

  .brand { position: absolute; left: 0; right: 0; display: flex; align-items: center; justify-content: center; gap: 14px; }
  .brand__mark { border-radius: 50%; border: 3px solid var(--gold); flex: none; }
  .brand__name { font-family: "Questrial", sans-serif; color: var(--gold); white-space: nowrap; }
  .card--front .brand { top: 132px; }
  .card--front .brand__mark { width: 34px; height: 34px; }
  .card--front .brand__name { font-size: 40px; }
  .card--back .brand { top: 98px; }
  .card--back .brand__mark { width: 48px; height: 48px; }
  .card--back .brand__name { font-size: 56px; }

  .holder { position: absolute; top: 178px; left: 0; right: 0; text-align: center;
    font-family: "Questrial", sans-serif; font-size: 41px; color: var(--ink); }

  .rule { position: absolute; left: 0; right: 0; top: 246px; height: 16px; background: var(--plum-dark); }
  .contact-band { position: absolute; left: 0; right: 0; top: 262px; bottom: 0; background: var(--plum); }
  .card--back .contact-band { top: 245px; }

  .contact { position: absolute; top: 46px; width: 280px; margin-left: -140px; text-align: center; color: var(--on-plum);
    font-family: "Hind", sans-serif; font-size: 24px; }
  .contact svg { display: block; margin: 0 auto 30px; }
  .contact--phone { left: 164px; }
  .contact--mail { left: 431px; }
  .contact--web { left: 697px; }

  .web-line { position: absolute; top: 110px; left: 0; right: 0; display: flex; align-items: center; justify-content: center; gap: 26px;
    color: var(--on-plum); font-family: "Hind", sans-serif; font-size: 25px; }
</style>
</head>
<body>
<div class="canvas">

  <section class="card card--front">
    <div class="brand" style="top:60px"><span class="brand__mark"></span><span class="brand__name">Klarweg Mediation</span></div>
    <h1 class="holder" style="font-weight:400">Sabine Fellor di Vanti</h1>
    <div class="rule"></div>
    <div class="contact-band">
      <div class="contact contact--phone">
        <svg width="46" height="46" viewBox="0 0 46 46" fill="none" stroke="#fff" stroke-width="2"><circle cx="23" cy="23" r="21.5"/><path d="M15 14c2-2 4-1 5 1l1 3c0 1-1 2-2 3 1 3 3 5 6 6 1-1 2-2 3-2l3 1c2 1 3 3 1 5-2 2-5 2-8 0-4-2-7-5-9-9-2-3-2-6 0-8z" fill="#fff" stroke="none"/></svg>
        076 412 58 94
      </div>
      <div class="contact contact--mail">
        <svg width="46" height="46" viewBox="0 0 46 46" fill="none" stroke="#fff" stroke-width="2"><circle cx="23" cy="23" r="21.5"/><rect x="12" y="15" width="22" height="16" fill="#fff" stroke="none"/><path d="M12 15l11 9 11-9M12 31l8-7M34 31l-8-7" stroke="#6f3650" stroke-width="1.6"/></svg>
        sfellor@postkiv.ch
      </div>
      <div class="contact contact--web">
        <svg width="46" height="46" viewBox="0 0 46 46" fill="none" stroke="#fff" stroke-width="2"><circle cx="23" cy="23" r="21.5"/><g stroke-width="1.4"><circle cx="23" cy="23" r="12"/><ellipse cx="23" cy="23" rx="5.5" ry="12"/><path d="M11 23h24M13 17h20M13 29h20M23 11v24"/></g></svg>
        www.fellor-di-vanti.ch
      </div>
    </div>
  </section>

  <section class="card card--back">
    <div class="brand"><span class="brand__mark"></span><span class="brand__name">Klarweg Mediation</span></div>
    <div class="contact-band">
      <div class="web-line">
        <svg width="34" height="34" viewBox="0 0 34 34" fill="none" stroke="#fff" stroke-width="1.6"><circle cx="17" cy="17" r="15.5"/><ellipse cx="17" cy="17" rx="7" ry="15.5"/><path d="M1.5 17h31M4 9.5h26M4 24.5h26M17 1.5v31"/></svg>
        <span>www.fellor-di-vanti.ch</span>
      </div>
    </div>
  </section>

</div>
</body>
</html>
```